Homeowners Insurance Provider Website

We are selling homeowners insurance policy / tenants Policy/Flood Insurance in USA in few states and planning expand nationally.

Our target audience are two folds: Customers (Buy policies) and Insurance Agents who wants to work with us to sell our policies to customers. But website should focus 80% on customers and 20% on agents. So, more customer focused user experience. Please note that there is no direct buy option for customers. They always go through insurance agents.

Customer focused, educational that makes buyer journey easy. We don’t want to come off as trying sell something as there is no direct sales involved from website.

Target Market(s)

Homeowners in USA and Insurance agent who sells these insurance.

Industry/Entity Type

Insurance

Number of Pages Required

4 page

Font styles to use
Other font styles liked:
• Open to suggestions

Colors

Designer to choose colors to be used in the design.

Requirements
Must have
• Three most important things: Trustworthy, Authentic, Simple
• Please use colors form logo and grays
• We like: www.brightmeadow.com
• https://www.harborlinden.com/
• We need Agent Look up tool on home page similar to what is shown on example sites.
• Design:
• Home Page - Open to Ideas
• Insurance (Products) Landing Page - Info similar to: https://www.harborlinden.com/insurance/
• Agents Page - https://www.harborlinden.com/agents/
• Claims Page - Information similar to: https://www.harborlinden.com/claims-center/
• Site Navigation:
• Home
• Insurance
• Claims
• Agents
• About Us
• Contact Us
Nice to have
• Elegant, minimal and clean design that reflects trust and authenticity.
Should not have
• Slider or rotating images - prefer flat design. Not over powering design.

```html
<!DOCTYPE html>
<html lang="en">
<head>
<meta charset="utf-8">
<title>Hearthline Mutual — Home</title>
<link rel="stylesheet" href="https://fonts.googleapis.com/css2?family=Montserrat:wght@500;600;700&family=Open+Sans:wght@400;600&display=swap">
<style>
:root{
  --red:#c81f2e;
  --blue:#1f3b8f;
  --ink:#2b2b2b;
  --gray-text:#6b6b6b;
  --gray-line:#d9d9d9;
  --footer-bg:#eeeeee;
  --white:#ffffff;
}
*{box-sizing:border-box;margin:0;padding:0}
html,body{width:758px;height:1200px;overflow:hidden;background:var(--white)}
body{font-family:"Open Sans",Arial,sans-serif;color:var(--ink);position:relative}
.heading{font-family:"Montserrat",Arial,sans-serif}

/* top navigation */
.site-nav{height:50px;display:flex;align-items:center;justify-content:space-between;padding:0 28px;background:var(--white)}
.nav-links{display:flex;gap:26px;list-style:none;font-family:"Montserrat",Arial,sans-serif;font-weight:600;font-size:8px;letter-spacing:.5px;color:var(--ink)}
.brand{display:flex;align-items:center;gap:7px}
.brand-mark{width:10px;height:10px;border-radius:50%;background:var(--red)}
.brand-name{font-family:"Montserrat",Arial,sans-serif;font-weight:600;font-size:12px;line-height:1;color:var(--ink);white-space:nowrap}

/* hero */
.hero{position:relative;height:325px}
.hero-photo{position:absolute;inset:0;background:linear-gradient(100deg,#8b8f86 0%,#c7b9a6 30%,#d9d4cc 55%,#7c8a74 100%)}
.hero-panel{position:absolute;left:482px;top:32px;width:256px;height:226px;background:rgba(200,31,46,.88);padding:36px 22px;color:var(--white)}
.hero-title{font-size:27px;font-weight:700;line-height:1.08;letter-spacing:.3px}
.hero-text{font-size:8.5px;line-height:1.5;margin:12px 0 16px;max-width:205px}
.btn{display:inline-block;font-family:"Montserrat",Arial,sans-serif;font-weight:600;font-size:7px;letter-spacing:.6px;padding:6px 12px;border-radius:12px}
.btn-light{border:1px solid var(--white);color:var(--white)}
.btn-dark{border:1px solid var(--gray-line);color:var(--ink)}

/* audience cards */
.audience{display:flex;height:162px}
.audience-card{flex:1;display:flex;align-items:center;gap:18px;padding:0 28px;color:var(--white)}
.audience-card.customers{background:var(--red)}
.audience-card.agents{background:var(--blue)}
.audience-icon{flex:none;width:78px;height:88px}
.audience-title{font-size:13px;font-weight:700;letter-spacing:.5px}
.audience-text{font-size:8px;line-height:1.5;margin:6px 0 10px;max-width:230px}

/* products */
.products{padding-top:32px}
.section-title{text-align:center;font-size:18px;font-weight:700;letter-spacing:.6px;color:var(--ink)}
.section-rule{width:34px;height:2px;background:var(--red);margin:8px auto 0}
.product-grid{display:flex;gap:13px;padding:26px 40px 0}
.product-card{width:160px;height:270px;border:1px solid #e6e6e6;text-align:center;position:relative;background:var(--white)}
.product-photo{height:110px}
.photo-home{background:linear-gradient(160deg,#9fb3c6,#7d8b6e)}
.photo-renters{background:linear-gradient(160deg,#c9b8a3,#8e7b66)}
.photo-dwelling{background:linear-gradient(160deg,#b69a7d,#5e4a3a)}
.photo-agent{background:linear-gradient(160deg,#d8cfc6,#8f8c8a)}
.product-badge{width:34px;height:34px;border-radius:50%;background:var(--red);margin:-17px auto 0;position:relative;display:flex;align-items:center;justify-content:center;border:2px solid var(--white)}
.product-title{font-size:9px;font-weight:700;margin-top:10px;letter-spacing:.4px}
.product-text{font-size:7.5px;line-height:1.55;color:var(--gray-text);padding:7px 14px 0}
.product-card .btn{position:absolute;bottom:16px;left:50%;transform:translateX(-50%);white-space:nowrap}

/* footer */
.site-footer{position:absolute;left:0;top:925px;width:758px;height:275px;background:var(--footer-bg)}
.footer-brand{display:flex;justify-content:center;margin-top:46px}
.footer-cols{display:flex;justify-content:space-between;padding:32px 70px 0 95px}
.footer-col h4{font-family:"Montserrat",Arial,sans-serif;font-size:8px;font-weight:700;letter-spacing:.5px;margin-bottom:8px}
.footer-col ul{list-style:none}
.footer-col li{font-size:6.5px;color:var(--gray-text);line-height:1;margin-bottom:7px;display:flex;align-items:center;gap:5px;text-transform:uppercase}
.footer-col li::before{content:"";width:0;height:0;border-left:4px solid var(--red);border-top:3px solid transparent;border-bottom:3px solid transparent}
.footer-bottom{position:absolute;left:40px;right:40px;bottom:20px;border-top:1px solid var(--gray-line);padding-top:12px;text-align:center;font-size:6.5px;letter-spacing:.5px;color:var(--gray-text)}
</style>
</head>
<body>

<header class="site-nav">
  <ul class="nav-links"><li>HOME</li><li>INSURANCE</li><li>CLAIMS</li></ul>
  <div class="brand"><span class="brand-mark"></span><span class="brand-name">Hearthline Mutual</span></div>
  <ul class="nav-links"><li>AGENTS</li><li>ABOUT US</li><li>CONTACT US</li></ul>
</header>

<section class="hero">
  <div class="hero-photo" role="img" aria-label="Smiling couple embracing in front of their suburban house"></div>
  <div class="hero-panel">
    <h1 class="hero-title heading">HOME OWNERS<br>INSURANCE</h1>
    <p class="hero-text">Trusted coverage for the place you call home, offered through local agents who know your neighborhood.</p>
    <span class="btn btn-light">GET A QUOTE</span>
  </div>
</section>

<section class="audience">
  <div class="audience-card customers">
    <svg class="audience-icon" viewBox="0 0 78 88" fill="none" stroke="#fff" stroke-width="2">
      <path d="M39 3 L73 15 V44 C73 64 58 78 39 85 C20 78 5 64 5 44 V15 Z"/>
      <circle cx="39" cy="36" r="9"/>
      <path d="M23 62 C25 52 32 48 39 48 C46 48 53 52 55 62"/>
    </svg>
    <div>
      <h2 class="audience-title heading">CUSTOMERS</h2>
      <p class="audience-text">Learn what a homeowners policy covers and find a local agent who can help you choose.</p>
      <span class="btn btn-light">LEARN MORE</span>
    </div>
  </div>
  <div class="audience-card agents">
    <svg class="audience-icon" viewBox="0 0 78 88" fill="none" stroke="#fff" stroke-width="2">
      <path d="M39 3 L73 15 V44 C73 64 58 78 39 85 C20 78 5 64 5 44 V15 Z"/>
      <rect x="21" y="32" width="36" height="26" rx="2"/>
      <path d="M32 32 V27 H46 V32 M21 43 H57"/>
    </svg>
    <div>
      <h2 class="audience-title heading">INSURANCE AGENTS</h2>
      <p class="audience-text">Partner with us to offer dependable home coverage to your clients across a growing list of states.</p>
      <span class="btn btn-light">LEARN MORE</span>
    </div>
  </div>
</section>

<section class="products">
  <h2 class="section-title heading">OUR PRODUCTS</h2>
  <div class="section-rule"></div>
  <div class="product-grid">
    <article class="product-card">
      <div class="product-photo photo-home" role="img" aria-label="Two-storey family house with front lawn"></div>
      <div class="product-badge"><svg width="16" height="16" viewBox="0 0 16 16" fill="none" stroke="#fff" stroke-width="1.6"><path d="M3 8.5 L6.5 12 L13 4"/></svg></div>
      <h3 class="product-title heading">HOMEOWNERS</h3>
      <p class="product-text">Protect your house, belongings and liability with coverage shaped around how you live.</p>
      <span class="btn btn-dark">READ MORE</span>
    </article>
    <article class="product-card">
      <div class="product-photo photo-renters" role="img" aria-label="Agent handing keys to new tenants"></div>
      <div class="product-badge"><svg width="16" height="16" viewBox="0 0 16 16" fill="none" stroke="#fff" stroke-width="1.6"><circle cx="5" cy="8" r="3"/><path d="M8 8 H14 M12 8 V11"/></svg></div>
      <h3 class="product-title heading">RENTERS/CONDO</h3>
      <p class="product-text">Cover your personal items and liability whether you rent an apartment or own a condo.</p>
      <span class="btn btn-dark">READ MORE</span>
    </article>
    <article class="product-card">
      <div class="product-photo photo-dwelling" role="img" aria-label="House at dusk with warm lights"></div>
      <div class="product-badge"><svg width="16" height="16" viewBox="0 0 16 16" fill="none" stroke="#fff" stroke-width="1.6"><path d="M8 2 C10 5 12 7 12 10 A4 4 0 0 1 4 10 C4 7.5 6 6.5 8 2 Z"/></svg></div>
      <h3 class="product-title heading">DWELLING FIRE</h3>
      <p class="product-text">Coverage for rental and secondary homes against fire, wind and other named perils.</p>
      <span class="btn btn-dark">READ MORE</span>
    </article>
    <article class="product-card">
      <div class="product-photo photo-agent" role="img" aria-label="Agent meeting with a couple at a table"></div>
      <div class="product-badge"><svg width="16" height="16" viewBox="0 0 16 16" fill="none" stroke="#fff" stroke-width="1.6"><path d="M8 15 C4 10 3 8 3 6 A5 5 0 0 1 13 6 C13 8 12 10 8 15 Z"/><circle cx="8" cy="6" r="1.8"/></svg></div>
      <h3 class="product-title heading">AGENT LOCATOR TOOL</h3>
      <p class="product-text">Enter your zip code to find a licensed agent near you who offers our policies.</p>
      <span class="btn btn-dark">READ MORE</span>
    </article>
  </div>
</section>

<footer class="site-footer">
  <div class="footer-brand"><div class="brand"><span class="brand-mark"></span><span class="brand-name">Hearthline Mutual</span></div></div>
  <div class="footer-cols">
    <div class="footer-col"><h4>INSURANCE</h4><ul><li>Homeowners</li><li>Renters/Condo</li><li>Dwelling Fire</li><li>Agent Locator Tool</li></ul></div>
    <div class="footer-col"><h4>AGENTS</h4><ul><li>Overview</li><li>Value of an Agent</li><li>Become an Agent</li><li>For Agents</li></ul></div>
    <div class="footer-col"><h4>ABOUT US</h4><ul><li>Company Overview</li><li>History Timeline</li><li>Leadership</li><li>Blog</li></ul></div>
    <div class="footer-col"><h4>CUSTOMER SUPPORT</h4><ul><li>Contact Page</li><li>Links to Forms and Resources</li><li>Report a Claim Line</li><li>Find an Agent Line</li></ul></div>
  </div>
  <div class="footer-bottom">© 2018 HEARTHLINE MUTUAL &nbsp;|&nbsp; ALL RIGHTS RESERVED</div>
</footer>

</body>
</html>
```